New Zealand Marlborough Sauvignon Blanc wine packaging design

We need packaging design for our new wine brand, Dunmore Hale. The wine is a New Zealand Marlborough Sauvignon Blanc. We would like the packaging will portray elegance and style with an understated label. We are looking for a label that portrays the elegance of the French Riviera. The label should be round or pill shaped.
Updates

Industry/Entity Type

Wine

Font styles to use
Serif
Sans Serif

Requirements
Must have
• The words in order of importance: Dunmore Hale, Sauvignon Blanc, Marlborough, New Zealand. It should be fit to the bottle posted in the links
Nice to have
• a pill shape or circular shape
Should not have
• Illustrations of wine bottles, wine glasses, or grapes

```html
<!DOCTYPE html>
<html lang="en">
<head>
<meta charset="utf-8">
<title>Dunmore Hale Sauvignon Blanc Label</title>
<link href="https://fonts.googleapis.com/css2?family=Marcellus&family=Arimo:wght@400&display=swap" rel="stylesheet">
<style>
  :root {
    --ground: #000000;
    --ink: #ffffff;
    --sky: #dfe7f0;
    --cloud: #f3efe6;
    --hills: #7f88b8;
    --sea: #3f6fb0;
    --sea-light: #6fa0cf;
    --garden: #6f9a45;
    --bloom: #9aa64f;
  }
  html, body {
    margin: 0;
    padding: 0;
    width: 705px;
    height: 1200px;
    overflow: hidden;
    background: var(--ground);
  }
  .canvas {
    width: 705px;
    height: 1200px;
    display: block;
  }
  .label-frame {
    fill: var(--ground);
    stroke: var(--ink);
    stroke-width: 2.5;
  }
  .scene-window {
    stroke: var(--ink);
    stroke-width: 2;
  }
  .brand-name {
    font-family: "Marcellus", serif;
    font-size: 42px;
    letter-spacing: 3px;
    fill: var(--ink);
  }
  .variety-name {
    font-family: "Marcellus", serif;
    font-size: 32px;
    letter-spacing: 1.5px;
    fill: var(--ink);
  }
  .origin-line {
    font-family: "Arimo", sans-serif;
    font-size: 17px;
    letter-spacing: 1px;
    fill: var(--ink);
  }
</style>
</head>
<body>
<svg class="canvas" viewBox="0 0 705 1200" xmlns="http://www.w3.org/2000/svg">
  <defs>
    <linearGradient id="riviera-tones" x1="0" y1="0" x2="0" y2="1">
      <stop offset="0" stop-color="var(--sky)"/>
      <stop offset="0.18" stop-color="var(--cloud)"/>
      <stop offset="0.32" stop-color="var(--hills)"/>
      <stop offset="0.42" stop-color="var(--sea-light)"/>
      <stop offset="0.58" stop-color="var(--sea)"/>
      <stop offset="0.72" stop-color="var(--garden)"/>
      <stop offset="1" stop-color="var(--bloom)"/>
    </linearGradient>
    <path id="brand-arc" d="M138,600 A214 252 0 0 1 566,600"/>
    <path id="variety-arc" d="M108,600 A244 282 0 0 0 596,600"/>
  </defs>

  <g class="wine-label">
    <ellipse class="label-frame" cx="352" cy="600" rx="256" ry="306"/>

    <ellipse class="scene-window" cx="352" cy="600" rx="200" ry="238"
             fill="url(#riviera-tones)" role="img"
             aria-label="Painted Riviera coastline: cloudy sky, blue hills, a calm bay with boats, cypress trees and flowering gardens"/>

    <text class="brand-name" text-anchor="middle">
      <textPath href="#brand-arc" startOffset="50%">DUNMORE HALE</textPath>
    </text>

    <text class="variety-name" text-anchor="middle">
      <textPath href="#variety-arc" startOffset="50%">SAUVIGNON BLANC</textPath>
    </text>

    <text class="origin-line" text-anchor="middle" transform="translate(128 600) rotate(-90)">MARLBOROUGH</text>
    <text class="origin-line" text-anchor="middle" transform="translate(576 600) rotate(90)">NEW ZEALAND</text>
  </g>
</svg>
</body>
</html>
```